London Based Property Finding Company - have logo already

We find property for private purchasers and investors in London, UK.  We work for the BUYER, whereas estate agencies/real estate companies work for the seller. We offer a much more personalised service to UK and overseas purchasers.

We would like the following:

*A double sided business card

*A letterhead

We have attached two versions of the logo. Each logo style is set on two different coloured backgrounds. Please choose one of the two designs, whichever you prefer or feel more comfortable with, and produce one in black and one in white background.

This applies to both pieces of stationery.

THE BUSINESS CARD:

We would like the company name placed on its own on one side of the card and the contact details and what we do on the other.

e.g.

SIDE 1:

BRAMWELL PROPERTY FINDERS

SIDE 2:

Owen Bramwell

t: 0208 394 2860

m: +44(0)7932 418 507

e: info@bramwellpropertyfinders.co.uk

w: bramwellpropertyfinders.co.uk

London Property Finders and Search Agents

I will leave the layout up to you, but a minimalist layout is preferred. If you would like to put additional detial or design on the card then that is up to, but not specified.

It is optional to have the company name on side 2, but if you do use it, please make it smaller. than on the 1st side.

The design needs to be simple, professional and not too in your face.

If you are using the black background design on side 1 for the logo, then maybe a white backgounnd can be used on side 2 with a black typeface.

The type face for the contacts details should be sans serif standard typeface. Please experiment with the desciprtion.

-

THE LETTERHEAD;

You can experiment with the layout for the letterhead. e.g logo centre aligned on the top of the page with the contact details and address at the bottom of the page OR the logo, description running along a bar on the top of the page with the contact details and website address at the bottom. Please try and experiment with this, but the less 'busy', the better.

Here is info that needs to be on the letterhead.

Bramwell Property Finders

t: 0208 394 2860

m: +44(0)7932 418 507

(PLEASE NOTE; the below company info must be placed at the bottom of the page as a footer, in small text.)

Kestrand Holdings Ltd Trading as Bramwell Property Finders, a company registered in England & Wales, No.7351926 , Registered office is 41 Hollinmoor Court, Hollinmoor Road, London, SW9 3PL, t: 0208 394 2860, m: +44(0)7932 418 507, e: info@bramwellpropertyfinders.co.uk

Best of luck!

Thank you

Dear Designer,

I have now attached the supporting files to this brief.

Thanks,

Owen Bramwell
Bramwell Property Finders

```html
<!DOCTYPE html>
<html lang="en">
<head>
<meta charset="utf-8">
<title>Bramwell Property Finders – Stationery</title>
<link rel="stylesheet" href="https://fonts.googleapis.com/css2?family=Questrial&display=swap">
<style>
  :root {
    --navy: #1f3564;
    --claret: #7a1a1f;
    --ink: #1e1e1e;
    --card-black: #0c0c0c;
    --paper: #ffffff;
    --edge: #c8c8c8;
    --sans: "Questrial", "Century Gothic", sans-serif;
  }
  * { margin: 0; padding: 0; box-sizing: border-box; }
  html, body { width: 849px; height: 1200px; overflow: hidden; background: var(--paper); }
  body { position: relative; font-family: var(--sans); color: var(--ink); }

  .card { position: absolute; top: 80px; width: 260px; height: 159px; }
  .card--front { left: 65px; background: var(--card-black); }
  .card--back { left: 413px; background: var(--paper); border: 1px solid var(--edge); }

  .wordmark { position: absolute; white-space: nowrap; font-family: var(--sans); letter-spacing: 0.08em; }
  .card--front .wordmark { left: 0; right: 0; top: 72px; text-align: center; color: #fff; font-size: 12px; }
  .card--back .wordmark { left: 19px; top: 18px; color: var(--navy); font-size: 9.5px; }

  .holder { position: absolute; left: 19px; top: 52px; color: var(--navy); font-size: 10.5px; }
  .contacts { position: absolute; list-style: none; }
  .contacts li { white-space: nowrap; }
  .contacts .label { color: var(--claret); display: inline-block; }
  .card--back .contacts { left: 19px; top: 78px; font-size: 8.6px; line-height: 11.3px; }
  .card--back .contacts .label { width: 12px; }
  .tagline { position: absolute; left: 19px; top: 133px; color: var(--navy); font-size: 8.8px; white-space: nowrap; }

  .letterhead { position: absolute; left: 65px; top: 290px; width: 609px; height: 861px; border: 1px solid var(--edge); background: var(--paper); }
  .letterhead .wordmark { left: 31px; top: 30px; color: var(--navy); font-size: 19px; }
  .letterhead .company { position: absolute; left: 31px; top: 728px; color: var(--navy); font-size: 12px; white-space: nowrap; }
  .letterhead .contacts { left: 31px; top: 750px; font-size: 9.6px; line-height: 13.3px; }
  .letterhead .contacts .label { width: 14px; }
  .legal { position: absolute; left: 31px; top: 817px; font-size: 7.6px; line-height: 10.2px; color: var(--ink); white-space: nowrap; }
</style>
</head>
<body>
  <section class="card card--front" aria-label="Business card, front">
    <p class="wordmark">BRAMWELL PROPERTY FINDERS</p>
  </section>

  <section class="card card--back" aria-label="Business card, back">
    <p class="wordmark">BRAMWELL PROPERTY FINDERS</p>
    <p class="holder">Owen Bramwell</p>
    <ul class="contacts">
      <li><span class="label">t.</span>0208 394 2860</li>
      <li><span class="label">m.</span>+44(0)7932 418 507</li>
      <li><span class="label">e.</span>info@bramwellpropertyfinders.co.uk</li>
      <li><span class="label">w.</span>bramwellpropertyfinders.co.uk</li>
    </ul>
    <p class="tagline">London Property Finders and Search Agents</p>
  </section>

  <section class="letterhead" aria-label="Letterhead">
    <p class="wordmark">BRAMWELL PROPERTY FINDERS</p>
    <p class="company">Bramwell Property Finders</p>
    <ul class="contacts">
      <li><span class="label">t.</span>0208 394 2860</li>
      <li><span class="label">m.</span>+44(0)7932 418 507</li>
      <li><span class="label">e.</span>info@bramwellpropertyfinders.co.uk</li>
      <li><span class="label">w.</span>bramwellpropertyfinders.co.uk</li>
    </ul>
    <p class="legal">Kestrand Holdings Ltd Trading as Bramwell Property Finders, a company registered in England &amp; Wales, No.7351926, Registered office is<br>41 Hollinmoor Court, Hollinmoor Road, London, SW9 3PL, t: 0208 394 2860, m: +44(0)7932 418 507, e: info@bramwellpropertyfinders.co.uk</p>
  </section>
</body>
</html>
```